Pals of Wagtail Fundraiser Flyer for shelter dogs

Flyer for Fund Raiser for shelter and rescue dogsThis will be hosted by who we are calling Heroes First responders (Fire, Police, and EMS will be bartending raising money to help the shelter dogs).

I will be uploading a basic flyer I did but I don't like it, only showing for dates and words etc...

struggling to come up with something eye-catching related to the above.

We can keep the use of Heroes (spelled wrong on the flyer)but open for new ideas too and new title.

Target Market(s)

Animal lovers

Font styles to use
Serif
Sans Serif

Requirements
Must have
• the ties to first responders and dog rescue
• Must include First responder logo badges images. The image with the helping hands Maybe replace the badges with images of dogs or doggy paws something like that
• Must have a strong presence identifying and relating to first responders
• Images of first responders as well as even images of the first responder logos for fire department police department and EMS.
• The first responders are the ones hosting the event so we really want to raise them up and show their appreciation for the cause that is super important as well
• Title should read
• Guardians Guarding Pups

```html
<!DOCTYPE html>
<html lang="en">
<head>
<meta charset="utf-8">
<title>Guardians Guarding Pups – Fundraiser Flyer</title>
<link href="https://fonts.googleapis.com/css2?family=Gochi+Hand&family=Patrick+Hand&display=swap" rel="stylesheet">
<style>
  :root {
    --bg: #48b873;
    --paper: #ffffff;
    --red: #e32b12;
    --ink: #111111;
    --tan-light: #f3d9b8;
    --tan: #c98a4b;
    --white: #ffffff;
    --badge-silver: #d9d9d9;
    --badge-bronze: #c98a4b;
    --badge-gold: #e2c14f;
  }
  html, body {
    margin: 0;
    width: 1200px;
    height: 1200px;
    overflow: hidden;
    background: var(--bg);
  }
  .flyer {
    position: absolute;
    left: 190px;
    top: 20px;
    width: 820px;
    height: 1160px;
    background: var(--paper);
    overflow: hidden;
    box-shadow: 0 12px 40px rgba(0,0,0,.25);
    font-family: "Patrick Hand", sans-serif;
  }
  .event-date {
    position: absolute;
    left: 56px;
    top: 48px;
    margin: 0;
    font-family: "Gochi Hand", cursive;
    font-weight: 400;
    font-size: 64px;
    color: var(--ink);
    white-space: nowrap;
  }
  .org-mark {
    position: absolute;
    right: 56px;
    top: 56px;
    display: flex;
    align-items: center;
    gap: 12px;
  }
  .org-mark__dot {
    width: 46px;
    height: 46px;
    border-radius: 50%;
    background: var(--red);
  }
  .org-mark__name {
    font-size: 34px;
    color: var(--ink);
    white-space: nowrap;
  }
  .org-mark__sub {
    position: absolute;
    right: 56px;
    top: 110px;
    font-size: 15px;
    color: var(--ink);
    letter-spacing: .5px;
    white-space: nowrap;
  }
  .hero-photo {
    position: absolute;
    left: 100px;
    top: 170px;
    width: 270px;
    height: 390px;
    border-radius: 135px 135px 0 0;
    background: radial-gradient(ellipse at 50% 40%, var(--white) 0%, var(--tan-light) 45%, var(--tan) 100%);
  }
  .time-panel {
    position: absolute;
    left: 370px;
    top: 220px;
    width: 450px;
    height: 340px;
    background: var(--red);
    color: var(--white);
    text-align: center;
    white-space: nowrap;
  }
  .time-panel__hours { font-size: 80px; line-height: 1; margin-top: 58px; }
  .time-panel__lead { font-size: 28px; margin-top: 18px; }
  .time-panel__venue { font-size: 72px; line-height: 1; margin-top: 16px; }
  .event-title {
    position: absolute;
    left: 0;
    right: 0;
    top: 596px;
    margin: 0;
    text-align: center;
    font-family: "Gochi Hand", cursive;
    font-weight: 400;
    font-size: 58px;
    line-height: 1;
    color: var(--red);
    white-space: nowrap;
  }
  .event-copy {
    position: absolute;
    left: 90px;
    right: 90px;
    top: 684px;
    margin: 0;
    text-align: center;
    font-size: 23px;
    line-height: 1.3;
    color: var(--ink);
  }
  .responder-badges {
    position: absolute;
    left: 0;
    right: 0;
    top: 800px;
    display: flex;
    justify-content: center;
    gap: 60px;
  }
  .responder-badge {
    width: 150px;
    height: 150px;
    border: 4px solid var(--red);
    border-radius: 50%;
    display: flex;
    align-items: center;
    justify-content: center;
    box-sizing: border-box;
  }
  .footer {
    position: absolute;
    left: 0;
    bottom: 0;
    width: 820px;
    height: 200px;
  }
  .footer__band { position: absolute; inset: 0; }
  .footer__content {
    position: absolute;
    left: 0;
    right: 0;
    bottom: 34px;
    display: flex;
    align-items: center;
    justify-content: center;
    gap: 30px;
    color: var(--white);
  }
  .footer__web { display: flex; align-items: center; gap: 12px; font-size: 28px; white-space: nowrap; }
  .footer__divider { width: 2px; height: 70px; background: var(--white); }
  .footer__follow { font-size: 32px; line-height: 1; }
  .social-list { display: flex; gap: 10px; margin-top: 8px; }
  .social-list span { width: 24px; height: 24px; border-radius: 50%; background: var(--white); }
</style>
</head>
<body>
  <main class="flyer">
    <h2 class="event-date">AUG 15, 2019</h2>

    <div class="org-mark">
      <span class="org-mark__dot"></span>
      <span class="org-mark__name">Pals of Wagtail</span>
    </div>
    <div class="org-mark__sub">RIVERBEND COUNTY DOG POUND</div>

    <div class="hero-photo" role="img" aria-label="Photo of a tan and white shelter puppy"></div>

    <section class="time-panel">
      <div class="time-panel__hours">6-10pm</div>
      <div class="time-panel__lead">hosted at the</div>
      <div class="time-panel__venue">harbor club</div>
    </section>

    <h1 class="event-title">GUARDIANS GUARDING PUPS</h1>
    <p class="event-copy">join pals of wagtail for an evening of fun! come spend an evening with our celebrity bartenders and help some pups in need. Our local men and women in uniform will be pouring drinks and raising awarness of adoption.</p>

    <div class="responder-badges">
      <div class="responder-badge" role="img" aria-label="Fire department badge">
        <svg width="80" height="96" viewBox="0 0 80 96"><path d="M40 4 L74 20 L68 70 L40 92 L12 70 L6 20 Z" fill="var(--badge-bronze)"/></svg>
      </div>
      <div class="responder-badge" role="img" aria-label="Police badge">
        <svg width="90" height="96" viewBox="0 0 90 96"><path d="M45 4 L84 26 L76 72 L45 92 L14 72 L6 26 Z" fill="var(--badge-silver)"/></svg>
      </div>
      <div class="responder-badge" role="img" aria-label="EMS badge">
        <svg width="84" height="96" viewBox="0 0 84 96"><path d="M42 4 L80 22 L72 74 L42 92 L12 74 L4 22 Z" fill="var(--badge-gold)"/></svg>
      </div>
    </div>

    <footer class="footer">
      <svg class="footer__band" width="820" height="200" viewBox="0 0 820 200" preserveAspectRatio="none">
        <path d="M0 110 Q410 -10 820 30 L820 200 L0 200 Z" fill="var(--ink)"/>
      </svg>
      <div class="footer__content">
        <div class="footer__web">
          <svg width="26" height="26" viewBox="0 0 26 26" fill="none" stroke="#fff" stroke-width="2">
            <circle cx="13" cy="13" r="11"/><ellipse cx="13" cy="13" rx="5" ry="11"/><line x1="2" y1="13" x2="24" y2="13"/>
          </svg>
          <span>www.palsofwagtailriverbend.org</span>
        </div>
        <div class="footer__divider"></div>
        <div>
          <div class="footer__follow">Follow Us:</div>
          <div class="social-list"><span></span><span></span><span></span><span></span></div>
        </div>
      </div>
    </footer>
  </main>
</body>
</html>
```